Business Card Design - Law Firm

We are a boutique law firm located near the beach in Manly, Australia. We have recently had a new logo designed and are revamping our business cards with the new logo.

We have recently had a business card design done for us but are not entirely happy with it. We are looking for something modern, simplistic but striking. We would like to see multiple designs.

We have attached a word document which includes our new logo and the current business card design which we are looking at moving away from.

We would like the business cards to be double sided. We would like the design to include something which we can print in gloss colour when we send it to the business card printers.

```html
<!DOCTYPE html>
<html lang="en">
<head>
<meta charset="utf-8">
<title>Halden &amp; Associates – Business Card</title>
<link href="https://fonts.googleapis.com/css2?family=Roboto:wght@400;500;700&display=swap" rel="stylesheet">
<style>
  :root {
    --backdrop: #b9b9b9;
    --card: #f4f4f3;
    --navy: #1b2f6b;
    --blue: #4a6db0;
    --gold: #a99a6c;
    --ink: #1f1f1f;
    --soft-ink: #3a3a3a;
  }
  * { margin: 0; padding: 0; box-sizing: border-box; }
  html, body { width: 1200px; height: 576px; overflow: hidden; }
  body {
    background: var(--backdrop);
    font-family: "Roboto", sans-serif;
    position: relative;
  }
  .card {
    position: absolute;
    top: 142px;
    width: 484px;
    height: 292px;
    background: var(--card);
    border-radius: 14px;
    overflow: hidden;
    box-shadow: 0 3px 8px rgba(0,0,0,0.25);
  }
  .card--front { left: 82px; }
  .card--back {
    left: 602px;
    background: linear-gradient(120deg, #e9ebf0 0%, #f4f4f3 55%, #f1f0ec 100%);
  }

  /* Front */
  .brand {
    position: absolute;
    left: 0; right: 0;
    text-align: center;
    color: var(--ink);
  }
  .brand__dot {
    display: block;
    margin: 0 auto 18px;
    width: 64px; height: 64px;
    border-radius: 50%;
    background: var(--navy);
  }
  .brand__name {
    font-weight: 500;
    font-size: 21px;
    letter-spacing: 1.5px;
  }
  .card--front .brand { top: 66px; }
  .front-web {
    position: absolute;
    top: 250px; left: 0; right: 0;
    display: flex;
    align-items: center;
    justify-content: center;
    gap: 14px;
    font-size: 13px;
    color: var(--soft-ink);
  }
  .front-web__rule {
    width: 52px; height: 3px;
    background: linear-gradient(90deg, transparent, var(--blue));
    clip-path: polygon(0 40%, 100% 0, 100% 100%, 0 60%);
  }
  .front-web__rule--right { transform: scaleX(-1); }
  .front-band {
    position: absolute;
    left: 0; right: 0; bottom: 0;
    height: 12px;
    background: linear-gradient(90deg, var(--navy) 0%, var(--blue) 50%, var(--gold) 50.1%, #c2b48a 100%);
  }

  /* Back */
  .card--back .brand {
    top: 92px;
    left: 12px;
    right: auto;
    width: 222px;
  }
  .card--back .brand__dot { width: 50px; height: 50px; margin-bottom: 14px; }
  .card--back .brand__name { font-size: 16px; letter-spacing: 1px; }
  .contact {
    position: absolute;
    left: 247px;
    top: 56px;
    color: var(--ink);
  }
  .contact__name {
    font-weight: 700;
    font-size: 22px;
    color: var(--navy);
    line-height: 1.1;
  }
  .contact__role { font-size: 12.5px; margin-top: 6px; }
  .contact__address { font-size: 12.5px; line-height: 18px; margin-top: 18px; }
  .contact__lines { list-style: none; margin-top: 2px; font-size: 12.5px; line-height: 18.5px; }
  .contact__lines li { display: flex; align-items: center; gap: 10px; }
  .contact__lines svg { width: 12px; height: 12px; fill: var(--navy); flex: none; }
  .back-band-gold {
    position: absolute;
    left: 0; bottom: 0;
    width: 200px; height: 12px;
    background: linear-gradient(90deg, #c2b48a, var(--gold));
  }
  .back-band-blue {
    position: absolute;
    right: 0; bottom: 0;
    width: 290px; height: 36px;
    background: linear-gradient(90deg, var(--blue), var(--navy));
    clip-path: polygon(5% 0, 100% 0, 100% 100%, 0 100%);
    border-top-left-radius: 10px;
    color: #fff;
    font-size: 12.5px;
    display: flex;
    align-items: center;
    padding-left: 54px;
  }
</style>
</head>
<body>

<section class="card card--front">
  <div class="brand">
    <span class="brand__dot"></span>
    <p class="brand__name">Halden &amp; Associates</p>
  </div>
  <div class="front-web">
    <span class="front-web__rule"></span>
    <span>www.haldenandassociates.com.au</span>
    <span class="front-web__rule front-web__rule--right"></span>
  </div>
  <div class="front-band"></div>
</section>

<section class="card card--back">
  <div class="brand">
    <span class="brand__dot"></span>
    <p class="brand__name">Halden &amp; Associates</p>
  </div>

  <div class="contact">
    <h1 class="contact__name">Mara Ellison</h1>
    <p class="contact__role">Managing Director</p>
    <p class="contact__address">Suite 4, 12 Dune Street<br>Seacliff NSW 2099</p>
    <ul class="contact__lines">
      <li>
        <svg viewBox="0 0 12 12" aria-hidden="true"><path d="M1 3.5C1 2 3 1 6 1s5 1 5 2.5V5H8.5V3.8h-5V5H1z M2.5 6h7L11 11H1z"/></svg>
        (02) 9400 1100
      </li>
      <li>
        <svg viewBox="0 0 12 12" aria-hidden="true"><path d="M1 3.5C1 2 3 1 6 1s5 1 5 2.5V5H8.5V3.8h-5V5H1z M2.5 6h7L11 11H1z"/></svg>
        (02) 9400 1200
      </li>
      <li>
        <svg viewBox="0 0 12 12" aria-hidden="true"><path d="M0.5 2.5h11v7h-11z M1 3l5 4 5-4" fill="none" stroke="#1b2f6b" stroke-width="1.2"/></svg>
        mara.ellison@seacliffelaw.com.au
      </li>
    </ul>
  </div>

  <div class="back-band-gold"></div>
  <div class="back-band-blue">www.haldenandassociates.com.au</div>
</section>

</body>
</html>
```